Half page (a5) ad for a company

I need a design for an ad for a company to be published in a conference catalogue. Please find enclosed the logo for a company. The company is providing health screening services. Ad should be subtle and minimalistic, i.e. logo in the centre and a phrase saying: "Be in charge of your own health" and the website bluefern.co.uk. Also please find enclosed guidlines for colours and fonts to be used.

```html
<!DOCTYPE html>
<html lang="en">
<head>
<meta charset="utf-8">
<title>Blue Fern Private — Half Page Ad</title>
<link rel="stylesheet" href="https://fonts.googleapis.com/css2?family=Montserrat:wght@400;500;600&display=swap">
<style>
  :root {
    --brand-red: #e30613;
    --ink: #111111;
    --paper: #ffffff;
    --backdrop: #e0e0e0;
    --soft-grey: #f2f2f2;
  }
  * { margin: 0; padding: 0; box-sizing: border-box; }
  html, body {
    width: 1200px;
    height: 1200px;
    overflow: hidden;
    background: var(--backdrop);
  }
  .ad-page {
    position: absolute;
    left: 176px;
    top: 0;
    width: 848px;
    height: 1200px;
    background: var(--paper);
    overflow: hidden;
    font-family: "Montserrat", sans-serif;
  }
  .corner-curve {
    position: absolute;
    left: 0;
    bottom: 0;
    width: 50px;
    height: 215px;
  }
  .brand-mark {
    position: absolute;
    left: 50%;
    top: 150px;
    width: 200px;
    height: 200px;
    margin-left: -100px;
    border-radius: 50%;
    background: var(--brand-red);
  }
  .brand-name {
    position: absolute;
    left: 0;
    right: 0;
    top: 440px;
    text-align: center;
    font-weight: 400;
    font-size: 64px;
    line-height: 1;
    color: var(--brand-red);
  }
  .tagline-band {
    position: absolute;
    left: 0;
    right: 0;
    top: 731px;
    height: 220px;
    background: var(--brand-red);
    display: flex;
    align-items: center;
    justify-content: center;
  }
  .tagline {
    color: var(--paper);
    font-weight: 600;
    font-size: 66px;
    line-height: 78px;
    text-align: center;
    letter-spacing: 0.5px;
  }
  .website {
    position: absolute;
    left: 0;
    right: 0;
    top: 1082px;
    text-align: center;
    font-weight: 500;
    font-size: 30px;
    color: var(--ink);
  }
</style>
</head>
<body>
  <main class="ad-page">
    <svg class="corner-curve" viewBox="0 0 50 215" aria-hidden="true">
      <path d="M0 0 C30 60 50 130 40 215 L0 215 Z" fill="var(--soft-grey)"/>
    </svg>

    <div class="brand-mark" aria-hidden="true"></div>
    <h1 class="brand-name">Blue Fern Private</h1>

    <section class="tagline-band">
      <p class="tagline">Be in charge of<br>your own health</p>
    </section>

    <p class="website">bluefern.co.uk</p>
  </main>
</body>
</html>
```